Business cards Dorn Kelterhof GmbH & Co.KG

We need a uniform business card design template for our employees.
A template should be created to have the same design for all business cards.

Contact Information for Business Card

Firma und Firmierung, Name, Funktion in Unternehmen, Anschrift, Tel. Handynummer, Emailadresse, Internetseite

Colors

Designer to choose colors to be used in the design.

Requirements
Must have
• Our company logo must be on it

```html
<!DOCTYPE html>
<html lang="de">
<head>
<meta charset="utf-8">
<title>Dorn Kelterhof – Visitenkarte</title>
<link rel="stylesheet" href="https://fonts.googleapis.com/css2?family=EB+Garamond:wght@500;600&family=Arimo:wght@400&display=swap">
<style>
  :root {
    --stage: #ecebe8;
    --card-white: #ffffff;
    --lilac: #c9a0cc;
    --rose: #f06f80;
    --ink: #4a4a4a;
    --shadow: rgba(0, 0, 0, 0.22);
  }
  * { margin: 0; padding: 0; box-sizing: border-box; }
  html, body {
    width: 1125px; height: 1200px; overflow: hidden;
    background: var(--stage);
  }
  .canvas { position: relative; width: 1125px; height: 1200px; }

  .card {
    position: absolute; left: 162px; width: 800px; height: 455px;
    border-radius: 24px; overflow: hidden;
    box-shadow: 0 4px 10px var(--shadow);
  }
  .card--front { top: 95px; background: var(--card-white); }
  .card--back { top: 612px; background: var(--rose); }

  .brand-name {
    position: absolute; white-space: nowrap;
    font-family: "EB Garamond", serif; font-weight: 500;
  }
  .card--front .brand-name {
    left: 80px; top: 200px; font-size: 46px; color: var(--rose);
  }
  .card--back .brand-name {
    left: 0; right: 0; top: 178px; text-align: center;
    font-size: 72px; color: var(--card-white);
  }

  .divider {
    position: absolute; left: 438px; top: 113px;
    width: 1px; height: 232px; background: var(--lilac);
  }

  .contact { position: absolute; left: 470px; top: 106px; }
  .contact__name {
    font-family: "EB Garamond", serif; font-weight: 600;
    font-size: 27px; letter-spacing: 0.5px; color: var(--lilac);
    line-height: 1.1;
  }
  .contact__role {
    font-family: "Arimo", sans-serif; font-size: 17px;
    color: var(--rose); margin-top: 2px;
  }
  .contact__address {
    font-family: "Arimo", sans-serif; font-size: 17px;
    color: var(--ink); line-height: 22px; margin-top: 14px;
  }
  .contact__list { list-style: none; margin-top: 16px; }
  .contact__item {
    display: flex; align-items: center; gap: 8px;
    font-family: "Arimo", sans-serif; font-size: 17px;
    color: var(--ink); line-height: 22.5px;
  }
  .contact__icon { width: 18px; height: 18px; flex: none; }

  .accent-band {
    position: absolute; bottom: 0; height: 14px;
  }
  .accent-band--lilac { left: 0; width: 397px; background: var(--lilac); }
  .accent-band--rose { left: 401px; right: 0; background: var(--rose); }
</style>
</head>
<body>
<div class="canvas">

  <section class="card card--front">
    <div class="brand-name">Dorn Kelterhof</div>
    <div class="divider"></div>
    <div class="contact">
      <div class="contact__name">LUKAS BRANDT</div>
      <div class="contact__role">President</div>
      <div class="contact__address">2914 Willowbend Road<br>Fairview, Oregon 97024</div>
      <ul class="contact__list">
        <li class="contact__item">
          <svg class="contact__icon" viewBox="0 0 18 18"><circle cx="9" cy="9" r="9" fill="var(--lilac)"/><path d="M6 4.5l2 2-1 1.3c.6 1.3 1.6 2.3 2.9 2.9l1.3-1 2 2-1.3 1.6C8.6 13.3 4.7 9.4 4.7 6.1z" fill="#fff"/></svg>
          482-317-6040
        </li>
        <li class="contact__item">
          <svg class="contact__icon" viewBox="0 0 18 18"><circle cx="9" cy="9" r="9" fill="var(--lilac)"/><rect x="6" y="4" width="6" height="10" rx="1" fill="#fff"/><rect x="7" y="5.2" width="4" height="6.5" fill="var(--lilac)"/></svg>
          482-609-1273
        </li>
        <li class="contact__item">
          <svg class="contact__icon" viewBox="0 0 18 18"><circle cx="9" cy="9" r="9" fill="var(--lilac)"/><rect x="6" y="4.5" width="6" height="3" fill="#fff"/><rect x="4.5" y="8" width="9" height="4" rx="1" fill="#fff"/><rect x="6" y="11" width="6" height="2.5" fill="#fff"/></svg>
          482-754-8815
        </li>
        <li class="contact__item">
          <svg class="contact__icon" viewBox="0 0 18 18"><circle cx="9" cy="9" r="9" fill="var(--lilac)"/><rect x="4.5" y="5.5" width="9" height="7" fill="#fff"/><path d="M4.5 5.5L9 9.5l4.5-4" fill="none" stroke="var(--lilac)" stroke-width="1"/></svg>
          info@dornkelterhof.com
        </li>
        <li class="contact__item">
          <svg class="contact__icon" viewBox="0 0 18 18"><circle cx="9" cy="9" r="9" fill="var(--lilac)"/><circle cx="9" cy="9" r="4.5" fill="none" stroke="#fff" stroke-width="1.4"/><path d="M4.5 9h9M9 4.5c-2 2.5-2 6.5 0 9M9 4.5c2 2.5 2 6.5 0 9" fill="none" stroke="#fff" stroke-width="1"/></svg>
          www.dornkelterhof.com
        </li>
      </ul>
    </div>
    <div class="accent-band accent-band--lilac"></div>
    <div class="accent-band accent-band--rose"></div>
  </section>

  <section class="card card--back">
    <div class="brand-name">Dorn Kelterhof</div>
  </section>

</div>
</body>
</html>
```